K & D A/C Compressors' Business Card

Hello,

I need someone to create a new business card for my business. The name of my Business is: K & D A/C Compressors. I sell automotive air conditioning parts (a/c parts). I would like the business card to incorporate my logo, and to have an automotive feel to it. It is important that the business card feel like it is coming from an automotive parts business.

I already have a logo, which I will provide.

Thanks.
Updates

Project Deadline Extended Reason: I feel like extending the deadline until October 9, 2017, will allow for more time to design the business card. Thank you for your understanding. Added Monday, October 2, 2017

Target Market(s)

Consumers who need automotive a/c parts, and auto mechanics.

Industry/Entity Type

Automotive

Contact Information for Business Card

Business name: K & D A/C Compressors
Business Address: 48207 Southwest 36th Street, North Miami Beach, Florida 33162
Telephone: 305-472-1390
Fax: To be provided once I choose your design.
Website: www.kdcoolunits.example
Email: support@kdcoolunits.example
Names: To be provided once I choose your design.

Font styles to use
Sans Serif

Colors

Designer to choose colors to be used in the design.

Requirements
Must have
• The business card must include all of the "Business Card Details" and the logo I have uploaded.

```html
<!DOCTYPE html>
<html lang="en">
<head>
<meta charset="utf-8">
<title>K &amp; D A/C Compressors — Business Card</title>
<link href="https://fonts.googleapis.com/css2?family=Montserrat:wght@400;600&display=swap" rel="stylesheet">
<style>
  :root {
    --page: #e9eaec;
    --ink: #050505;
    --blue: #1a8fd6;
    --blue-deep: #0b4f8f;
    --blue-dark: #073a6e;
    --silver: #c9ccd0;
    --grey: #7d8085;
    --white: #f4f6f8;
  }
  * { margin: 0; padding: 0; box-sizing: border-box; }
  html, body { width: 1200px; height: 1200px; overflow: hidden; }
  body {
    background: var(--page);
    font-family: "Montserrat", sans-serif;
    display: flex;
    flex-direction: column;
    align-items: center;
    justify-content: center;
    gap: 70px;
  }
  .card {
    position: relative;
    width: 840px;
    height: 480px;
    overflow: hidden;
    box-shadow: 0 10px 30px rgba(0,0,0,0.18);
  }
  /* Front */
  .card--front { background: var(--ink); }
  .card__corners { position: absolute; inset: 0; }
  .brand-name {
    position: absolute;
    left: 70px;
    top: 190px;
    font-size: 40px;
    font-weight: 600;
    color: var(--grey);
    letter-spacing: 1px;
    line-height: 1.2;
  }
  .contact {
    position: absolute;
    left: 470px;
    top: 140px;
    color: var(--silver);
  }
  .contact__name {
    font-size: 34px;
    font-weight: 600;
    color: var(--white);
    letter-spacing: 1px;
  }
  .contact__role {
    font-size: 16px;
    color: var(--blue);
    margin-bottom: 32px;
  }
  .contact__address {
    font-size: 15px;
    line-height: 1.5;
    margin-bottom: 12px;
  }
  .contact__list { list-style: none; font-size: 15px; line-height: 1.75; }
  .contact__list li { display: flex; align-items: center; gap: 10px; }
  .contact__list svg { width: 15px; height: 15px; fill: var(--blue); flex: none; }
  /* Back */
  .card--back {
    background: linear-gradient(160deg, var(--blue) 0%, var(--blue-deep) 65%, var(--blue-dark) 100%);
    display: flex;
    align-items: center;
    justify-content: center;
  }
  .card--back .brand-name {
    position: static;
    font-size: 54px;
    color: var(--silver);
    text-align: center;
  }
</style>
</head>
<body>
  <section class="card card--front">
    <svg class="card__corners" viewBox="0 0 840 480" preserveAspectRatio="none" aria-hidden="true">
      <polygon points="0,0 560,0 0,80" fill="var(--blue)"/>
      <polygon points="840,480 300,480 840,390" fill="var(--blue)"/>
    </svg>
    <p class="brand-name">K &amp; D A/C<br>Compressors</p>
    <div class="contact">
      <h1 class="contact__name">JOHN DOE</h1>
      <p class="contact__role">Director</p>
      <p class="contact__address">48207 Southwest 36th Street<br>Coral Reef Bay, Florida 33990</p>
      <ul class="contact__list">
        <li><svg viewBox="0 0 16 16"><circle cx="8" cy="8" r="7" fill="none" stroke="var(--blue)" stroke-width="1.6"/><path d="M1 8h14M8 1c3 3 3 11 0 14M8 1c-3 3-3 11 0 14" fill="none" stroke="var(--blue)" stroke-width="1.2"/></svg>www.kdcoolunits.example</li>
        <li><svg viewBox="0 0 16 16"><rect x="1" y="3" width="14" height="10" rx="1"/><path d="M1 4l7 5 7-5" fill="none" stroke="#050505" stroke-width="1.3"/></svg>support@kdcoolunits.example</li>
        <li><svg viewBox="0 0 16 16"><path d="M3 1h3l1.5 4-2 1.3a9 9 0 0 0 4.2 4.2l1.3-2 4 1.5v3c0 1-1 2-2 2A13 13 0 0 1 1 3c0-1 1-2 2-2z"/></svg>305-472-1390</li>
        <li><svg viewBox="0 0 16 16"><rect x="4" y="1" width="8" height="5"/><rect x="1" y="6" width="14" height="7" rx="1"/><rect x="4" y="10" width="8" height="5" fill="#050505" stroke="var(--blue)"/></svg>xxx-xxx-xxxx</li>
      </ul>
    </div>
  </section>

  <section class="card card--back">
    <p class="brand-name">K &amp; D A/C Compressors</p>
  </section>
</body>
</html>
```